Trevor Outreach Group's Primary Marketing Brochure (Gate Fold Format)

We are looking for a main brochure design to communicate our company's primary mission, the need, where we meet the needs, how we meet the needs, and how the reader can get involved. We would like to see the color palette be similar to the colors of our company logo (attached). We would like to see a brochure design similar to a "gate fold" offering 22"x8.5" fully opened and 5.5"x8.5" when closed. Front panel, inside panels, full spread panel, and back panel. Required Text for each panel and usable picture suggestions are attached along with the company logo. The design should clean, contemporary, and emotionally compelling.

Target Market(s)

40-65 years old male and female, religious-minded

Industry/Entity Type

It Company

Font styles to use
Sans Serif

Requirements
Must have
• include text from attached WORD document.
• Clean, contemporary design
• Color in color palette of agency logo attached

```html
<!DOCTYPE html>
<html lang="en">
<head>
<meta charset="utf-8">
<title>Trevor Outreach Group – Gate Fold Brochure</title>
<link href="https://fonts.googleapis.com/css2?family=Open+Sans:wght@400;600;700&family=Cinzel:wght@600;700&display=swap" rel="stylesheet">
<style>
:root{
  --navy:#1d2f8f;
  --navy-dark:#16246f;
  --gold:#c9a246;
  --gold-light:#dcbd6e;
  --ink:#2b2b2b;
  --muted:#555;
  --paper:#ffffff;
  --paper-shade:#eeeeee;
  --stage:#e4e4e4;
}
*{box-sizing:border-box;margin:0;padding:0}
html,body{width:888px;height:1200px;overflow:hidden;background:var(--stage)}
body{position:relative;font-family:"Open Sans",Arial,sans-serif;color:var(--ink)}
ul{list-style:none}
.spread{position:absolute;left:20px;width:848px;height:328px;background:var(--paper);box-shadow:0 4px 14px rgba(0,0,0,.18);overflow:hidden}
.spread--outside{top:230px}
.spread--inside{top:640px}
.panel{position:absolute;top:0;height:328px;overflow:hidden}
.fold{position:absolute;top:0;width:1px;height:100%;background:rgba(0,0,0,.06)}
.tag{display:inline-block;background:var(--navy);color:#fff;font-size:6px;font-weight:700;text-transform:uppercase;padding:2px 6px 2px 5px;border-radius:0 8px 8px 0;letter-spacing:.2px}
.body-text{font-size:3.8px;line-height:5px;color:var(--muted)}
.body-text p{margin-bottom:2.5px}
.body-text li{position:relative;padding-left:6px;margin-bottom:2px}
.body-text li::before{content:"";position:absolute;left:1px;top:1.6px;width:2px;height:2px;background:var(--gold);border-radius:50%}
.brand{font-weight:700;color:var(--navy);letter-spacing:-.2px;display:flex;align-items:center;gap:4px}
.brand-dot{width:10px;height:10px;border-radius:50%;background:var(--navy);flex:none}
.photo{position:absolute}
/* outside spread */
.back{left:0;width:212px;padding:12px 10px 0 4px}
.back .tag{margin-bottom:3px}
.back .body-text{padding-left:6px;margin-bottom:4px}
.back-contact{position:absolute;left:10px;right:10px;bottom:14px}
.back-contact .brand{font-size:8px;margin-bottom:6px}
.contact-grid{display:grid;grid-template-columns:1fr 1fr 16px;gap:0 6px;font-size:3.6px;line-height:5px;color:var(--muted)}
.badge{grid-column:3;grid-row:1/4;width:14px;height:14px;border-radius:50%;background:#bbb;align-self:center}
.spread-map{left:212px;width:424px}
.map{left:20px;top:14px;width:384px;height:166px;background:radial-gradient(ellipse at 50% 45%,#d8b870 0%,#c9a246 55%,rgba(201,162,70,0) 72%)}
.countries{position:absolute;left:16px;top:186px;width:392px;display:grid;grid-template-columns:repeat(7,1fr);font-size:3.6px;line-height:5px;color:var(--muted);text-transform:uppercase}
.countries li{position:relative;padding-left:5px}
.countries li::before{content:"";position:absolute;left:0;top:1.6px;width:2px;height:2px;background:var(--gold)}
.stats-band{position:absolute;left:128px;top:224px;width:168px;text-align:center}
.stats-band span{display:inline-block;background:var(--navy);color:#fff;font-size:5.2px;font-weight:700;padding:2px 8px;border-radius:6px;text-transform:uppercase}
.stats{position:absolute;left:16px;top:242px;width:392px;display:grid;grid-template-columns:repeat(3,1fr);gap:8px}
.stats .body-text li::before{width:3px;height:2px;border-radius:0;background:var(--gold)}
.web-bar{position:absolute;left:0;bottom:0;width:424px;height:14px;background:var(--gold);color:var(--ink);font-size:5.5px;font-weight:600;letter-spacing:4px;text-align:center;line-height:14px}
.front{left:636px;width:212px;background:var(--paper)}
.front .brand{position:absolute;top:14px;left:40px;font-size:13px}
.front-circle{position:absolute;left:18px;top:50px;width:178px;height:178px;border-radius:50%;border:4px solid var(--gold);background:radial-gradient(circle at 50% 40%,#b4a67c,#8a5a3a 65%,#6e4a30);box-shadow:0 0 0 2px #fff inset}
.front-band{position:absolute;left:0;bottom:0;width:212px;height:130px}
.front-title{position:absolute;left:0;bottom:20px;width:212px;text-align:center;font-family:"Cinzel",Georgia,serif;font-weight:700;font-size:10px;line-height:12px;color:#fff;letter-spacing:.4px}
.front-title span{color:var(--gold-light)}
/* inside spread */
.p1{left:0;width:212px}
.p1-photo{left:0;top:0;width:212px;height:200px;background:linear-gradient(135deg,#b9a27a,#8c6a4a 55%,#5a4a3c);border-radius:0 0 170px 0;border-right:4px solid var(--gold);border-bottom:4px solid var(--gold)}
.p1 .tag{position:absolute;top:206px;left:0}
.p1 .body-text{position:absolute;top:218px;left:6px;right:8px}
.p1-close{position:absolute;left:6px;bottom:8px;font-size:4.6px;font-weight:600;color:var(--ink)}
.group-photo{left:212px;top:140px;width:424px;height:188px;background:linear-gradient(to bottom,rgba(255,255,255,1) 0%,rgba(190,196,180,.85) 28%,#7d8470 60%,#4f5448 100%)}
.p2,.p3{top:0;height:140px;padding:8px 10px 0 0}
.p2{left:212px;width:212px}
.p3{left:424px;width:212px}
.p2 .tag,.p3 .tag{margin-bottom:4px}
.item{padding-left:6px;margin-bottom:3px}
.item h3{font-size:5px;font-weight:700;color:var(--gold);text-transform:uppercase;line-height:6px}
.help strong{color:var(--navy)}
.help li::before{content:"✓";background:none;color:var(--gold);font-size:4px;top:0;left:0;width:auto;height:auto}
.p4{left:636px;width:212px;padding:8px 8px 0 4px}
.p4 .partner{font-size:4px;font-weight:700;color:var(--ink);margin-top:2px}
.p4-logo{position:absolute;top:52px;left:0;width:212px;display:flex;flex-direction:column;align-items:center}
.p4-logo .brand{font-size:11px}
.call{font-size:8px;font-weight:700;color:var(--navy);margin-top:10px;text-align:center;line-height:10px}
.call small{display:block;font-size:6px}
.p4-circle{position:absolute;left:30px;top:150px;width:230px;height:230px;border-radius:50%;border:4px solid var(--gold);background:radial-gradient(circle at 40% 40%,#8a6b52,#4c3a2e 60%,#3a2d25)}
.caption{position:absolute;left:52px;bottom:22px;color:#fff;font-size:7px;font-weight:600;line-height:9px}
.caption small{display:inline-block;background:var(--navy);font-size:4px;line-height:6px;padding:0 3px;margin-top:1px}
</style>
</head>
<body>

<section class="spread spread--outside" aria-label="Outside spread">
  <article class="panel back">
    <span class="tag">Vision of Trevor Outreach</span>
    <div class="body-text"><p>Our vision is ever more communities all around the world radically transformed by the love of the Gospel, with reproducing, multiplying, Christ-centered national leaders who are part of thriving local churches growing committed disciples of Jesus, boldly proclaiming the Good News and advancing the Kingdom in all aspects of society.</p></div>
    <span class="tag">Statement of Faith</span>
    <div class="body-text">
      <p><strong>We believe:</strong></p>
      <ul>
        <li>in the Scriptures of the Old and New Testament as inspired by God and inerrant in the original writings, the supreme and final authority in faith and life.</li>
        <li>in one God, eternally existing in three persons: Father, Son, and Holy Spirit.</li>
        <li>that Jesus Christ was begotten by the Holy Spirit and born of the virgin Mary and is true God and true man.</li>
        <li>that man was created in the image of God, that he sinned and thereby incurred not only physical death but also spiritual death, which is separation from God.</li>
        <li>that the Lord Jesus Christ died for our sins according to the Scriptures, as a representative and substitutionary sacrifice, and that all who believe in Him are justified.</li>
        <li>in the bodily resurrection of our crucified Lord, His ascension into heaven and His present life there for us as High Priest and Advocate.</li>
        <li>in that "blessed hope" — the personal and victorious return of our Lord and Savior, Jesus Christ.</li>
        <li>that all who receive by repentance and faith the Lord Jesus Christ are born again of the Holy Spirit and become children of God.</li>
        <li>in the bodily resurrection of the just and unjust, the everlasting blessedness of the saved and the everlasting punishment of the lost.</li>
        <li>that God created man and woman as unique biological persons made to complete each other, and that marriage is between one man and one woman as set out in Scripture.</li>
      </ul>
    </div>
    <div class="back-contact">
      <div class="brand"><span class="brand-dot"></span>Trevor Outreach Group</div>
      <div class="contact-grid">
        <span>1420 Ridgeview Rd, Meadowbrook,</span><span>www.trevoroutreach.org</span><span class="badge" aria-label="Partner seal"></span>
        <span>TN 37000</span><span>TrevorOutreach</span>
        <span>800-555-0148</span><span>TrevorOG</span>
      </div>
    </div>
  </article>
  <span class="fold" style="left:212px"></span>

  <article class="panel spread-map">
    <div class="photo map" role="img" aria-label="Gold world map marking the countries where national workers serve"></div>
    <ul class="countries">
      <li>Albania</li><li>Canada</li><li>Greece</li><li>Indonesia</li><li>Mexico</li><li>Philippines</li><li>Turkey</li>
      <li>Argentina</li><li>Costa Rica</li><li>Guatemala</li><li>Italy</li><li>Moldova</li><li>Romania</li><li>Uganda</li>
      <li>Australia</li><li>Cuba</li><li>Ghana</li><li>Kenya</li><li>Myanmar</li><li>South Africa</li><li>United States</li>
      <li>Bulgaria</li><li>Cyprus</li><li>Haiti</li><li>Lebanon</li><li>Pakistan</li><li>Spain</li><li>Zimbabwe</li>
      <li>Bangladesh</li><li>Egypt</li><li>India</li><li>Liberia</li><li>Peru</li><li>Thailand</li>
    </ul>
    <div class="stats-band"><span>Stats of needs from around the world</span></div>
    <div class="stats">
      <ul class="body-text"><li>3.1 billion people around the world are unreached and need to hear the Gospel</li><li>About 16,000 children under the age of five die each day from preventable causes</li><li>10.7% of the world's population lives on less than $1.90 per day</li></ul>
      <ul class="body-text"><li>1 out of every 113 people around the world is a refugee</li><li>1.2% of human trafficking victims are ever rescued</li><li>1.2 million children trafficked each year</li></ul>
      <ul class="body-text"><li>The average age of a human trafficking victim is 12. The average age a teen enters the sex trade is 12 to 14 years old. Many victims are runaway girls.</li><li>More than 85 percent of the pastors around the world have never received theological education or pastoral preparation</li></ul>
    </div>
    <div class="web-bar">www.trevoroutreach.org</div>
  </article>
  <span class="fold" style="left:636px"></span>

  <article class="panel front">
    <div class="brand"><span class="brand-dot"></span>Trevor Outreach Group</div>
    <svg class="front-band" viewBox="0 0 212 130" aria-hidden="true">
      <path d="M0 40 Q106 80 212 0 V130 H0 Z" fill="var(--navy)"/>
      <path d="M0 40 Q106 80 212 0" fill="none" stroke="var(--gold)" stroke-width="2"/>
    </svg>
    <div class="front-circle" role="img" aria-label="Photo of a child carrying water containers on a dirt road"></div>
    <h1 class="front-title">Equipping the Nations<br><span>with the Gospel</span></h1>
  </article>
</section>

<section class="spread spread--inside" aria-label="Inside spread">
  <article class="panel p1">
    <div class="photo p1-photo" role="img" aria-label="Photo of a mother holding her baby at a window"></div>
    <span class="tag">Who is a national worker?</span>
    <div class="body-text">
      <p>National workers are native missionaries who reach their own people with the Gospel. They are the hands and feet of Trevor Outreach Group in the countries where we minister.</p>
      <p>National workers are unique. Because they serve in their own countries, they don't need special government residence permits, and they are already experts with the local language and culture. They can even serve in countries where cross-cultural missionaries would not be allowed, and they serve at a fraction of the cost.</p>
      <p>National workers serve in a variety of ways to empower the local church and advance God's kingdom. Some are church planters and pastors. Some are teachers, school directors, house parents, and support staff at child and youth centers. Some serve in medical clinics as doctors and nurses, in media ministry, or in disaster relief. They are the key to sharing God's love in word and deed.</p>
    </div>
    <p class="p1-close">At the heart of every Trevor Outreach ministry is a national worker.</p>
  </article>

  <div class="photo group-photo" role="img" aria-label="Group photo of national workers holding newspapers in a park"></div>

  <article class="panel p2">
    <span class="tag">5 Areas of Ministry</span>
    <div class="item"><h3>1. Child Sponsorship</h3><p class="body-text">Our national workers verbally and visibly share the love of Christ to children which leads to transformed lives physically, intellectually, spiritually, emotionally, and socially.</p></div>
    <div class="item"><h3>2. Disciple Makers</h3><p class="body-text">We are helping to train pastors with resources typically unavailable to them as well as helping resource church planters as they advance the Gospel.</p></div>
    <div class="item"><h3>3. Medical Care</h3><p class="body-text">Showing the love of Christ to those in need can range from hospitals, training facilities, leprosy colonies, mobile units, and many clinics worldwide.</p></div>
    <div class="item"><h3>4. Media Evangelism</h3><p class="body-text">"Media" can take a wide variety of forms. We work through newspapers, internet, radio and other pieces of literature to share the Gospel in unreached areas.</p></div>
    <div class="item"><h3>5. Disaster Relief</h3><p class="body-text">We offer help when disasters such as earthquakes, hurricanes, tornadoes, and flooding occur as well as assisting Greece in the refugee crisis.</p></div>
  </article>
  <span class="fold" style="left:424px"></span>

  <article class="panel p3">
    <span class="tag">How can I help?</span>
    <div class="body-text help">
      <p style="padding-left:6px">Trevor Outreach Group relies on partners like you to assist in spreading the Gospel both in word and action to those in the most desperate of life circumstances. Partners participate by...</p>
      <ul style="padding-left:6px">
        <li><strong>Giving</strong>—Financially supporting our work through monthly, quarterly, annual, or one-time gifts. This can be done through our sponsorship programs or general support of the overall mission.</li>
        <li><strong>Going</strong>—Serve alongside a national worker on one of our many short-term mission team opportunities throughout the year; serve as a mission intern locally or on the foreign field, or even pray about serving as one of our long-term missionaries.</li>
        <li><strong>Praying</strong>—Join us in praying daily for the Lord's work happening through all of our ministries. Our monthly newsletter contains our daily prayer guide for suggestions on how to pray specifically for the work around the world.</li>
        <li><strong>Publicizing</strong>—Tell others about the great work you are supporting and connected to. Let your church know about the opportunity to partner with an organization that is advancing the Gospel worldwide. Share using social media to let others know all that is happening through your generosity and partnership.</li>
      </ul>
    </div>
  </article>
  <span class="fold" style="left:636px"></span>

  <article class="panel p4">
    <p class="body-text">Your partnership in giving, going, praying, and publicizing our mission is a key element that allows us to build upon our 75-year history of equipping national workers, empowering the local church, and transforming communities with the Gospel of Jesus Christ.</p>
    <p class="partner">Partner with Trevor Outreach Group Today!</p>
    <div class="p4-logo">
      <div class="brand"><span class="brand-dot"></span>Trevor Outreach Group</div>
      <p class="call">Call Us: 800-555-0148<small>www.trevoroutreach.org</small></p>
    </div>
    <div class="p4-circle" role="img" aria-label="Portrait photo of a national pastor"></div>
    <p class="caption">Daniel Okoth<br><small>National Pastor</small></p>
  </article>
</section>

</body>
</html>
```